Backflow Prevention Test Gauge Calibration Service

Our company, Northfield Valve Supply Company, specializes in backflow prevention, a backflow preventer is a valve on the public drinking water system that prevents contamination. Backflow preventers need to be tested annually using a backflow test gauge. A backflow test gauge is considered an instrument and is required to be tested and calibrated annually to ensure they are working accurately. We offer that service, along with repair services if the instrument is damaged, and we refer to it as a "Hassle Free" service. We schedule the service for them once they provide their information and then email them a shipping label that they can print out, tape on their box and send the package from their business or home. We have a quick-turnaround time for this service because we understand how important this piece of equipment is for our customers to continue their job.

The main points we want to highlight on the flyer are:
* Hassle free shipping
* 1-Day turnaround time
* Service all gauge models
* Price includes incoming & return freight
* Honor all manufacturer warranties

We would like to include the manufacturers' logos and photos of the gauges that our customers use and will recognize (photos in brief).

There are two ways to schedule this service with us. They can call us at (800) 642-3871 or they can fill out a form on our website www.pipeguardshop.com.

Our text preferences are Myriad Pro and Tahoma. Our brand colors are red, white and blue. Please visit our website to get an idea of our style too.

```html
<!DOCTYPE html>
<html lang="en">
<head>
<meta charset="utf-8">
<title>Backflow Prevention Test Gauge Calibration Service – Northfield Valve Supply Company</title>
<link href="https://fonts.googleapis.com/css2?family=Noto+Sans:wght@700;800&family=Source+Sans+3:wght@400;600;700&display=swap" rel="stylesheet">
<style>
  :root{
    --blue:#1b4d9c;
    --blue-deep:#0f3f8f;
    --red:#e41f2b;
    --ink:#222428;
    --grey:#5a5b5e;
    --rule:#b9bcc2;
    --white:#ffffff;
  }
  *{box-sizing:border-box;margin:0;padding:0}
  html,body{width:945px;height:1200px;overflow:hidden;background:#fff}
  .flyer{position:relative;width:945px;height:1200px;overflow:hidden;background:var(--white);
    font-family:"Source Sans 3",Arial,sans-serif;color:var(--ink)}

  .brand{position:absolute;left:50px;top:56px;display:flex;align-items:center;gap:14px}
  .brand-mark{width:58px;height:58px;border-radius:50%;background:var(--blue)}
  .brand-name{font-family:"Source Sans 3",sans-serif;font-weight:400;color:var(--blue);line-height:1}
  .brand-name .line1{display:block;font-size:35px}
  .brand-name .line2{display:block;font-size:17px;margin-top:4px}

  .tagline{position:absolute;left:56px;top:150px;font-family:"Noto Sans",sans-serif;font-weight:700;
    font-size:18px;color:var(--grey)}

  .rule-top{position:absolute;left:0;top:188px;width:560px;height:14px;
    background:linear-gradient(90deg,#a6a8ad,#e7e8ea 90%,#fff)}
  .title-band{position:absolute;left:0;top:202px;width:620px;height:255px;
    background:linear-gradient(90deg,var(--blue-deep),var(--blue))}
  .rule-bottom{position:absolute;left:0;top:457px;width:640px;height:20px;
    background:linear-gradient(90deg,#9d9fa4 0 40px,#d3d4d7 40px,#f2f2f3 85%,#fff)}
  .title{position:absolute;left:56px;top:232px;font-family:"Noto Sans",sans-serif;font-weight:800;
    font-size:39px;line-height:47px;color:var(--white);letter-spacing:-0.5px;
    text-shadow:2px 3px 4px rgba(0,0,0,.45)}

  .intro{position:absolute;left:57px;top:498px;width:490px;font-size:16px;font-weight:600;line-height:23px;color:var(--ink)}

  .why-head{position:absolute;left:57px;top:680px;width:266px;height:30px;
    background:linear-gradient(100deg,var(--blue) 0 86%,var(--red) 86% 93%,transparent 93%);
    color:var(--white);font-family:"Noto Sans",sans-serif;font-weight:800;font-size:18px;
    line-height:30px;padding-left:11px}

  .benefits{position:absolute;left:57px;top:718px;list-style:none}
  .benefit{position:relative;display:flex;align-items:center;height:38px;
    font-family:"Noto Sans",sans-serif;font-weight:800;font-size:17.5px;color:var(--blue);letter-spacing:.2px}
  .benefit::after{content:"";position:absolute;left:0;bottom:0;height:1px;background:var(--rule);width:var(--w)}
  .benefit:last-child::after{display:none}
  .benefit svg{width:26px;height:26px;margin-right:17px;flex:none}

  .details{position:absolute;left:55px;top:936px;width:530px;font-size:12.6px;line-height:19.4px;color:var(--ink)}
  .details strong{color:var(--red);font-weight:700}

  .makers{position:absolute;left:40px;top:1080px;display:flex;align-items:center;height:42px}
  .maker{font-family:"Source Sans 3",sans-serif;font-weight:700;color:var(--ink);padding:0 14px;
    border-right:1px solid var(--rule);line-height:42px;font-size:24px}
  .maker:last-child{border-right:none}

  .footer{position:absolute;left:0;top:1133px;width:945px;height:67px;background:var(--blue)}
  .footer-text{position:absolute;left:55px;top:1143px;font-family:"Noto Sans",sans-serif;font-weight:800;
    color:var(--white);font-size:14.5px;line-height:21px;letter-spacing:.1px}
  .footer-text .big{font-size:16.5px}
  .contact{position:absolute;left:593px;top:1116px;width:352px;height:84px;background:var(--red);
    border-top-left-radius:22px;text-align:center;color:var(--white);font-family:"Noto Sans",sans-serif;font-weight:800}
  .contact .phone{display:block;font-size:25px;line-height:30px;margin-top:10px}
  .contact .web{display:block;font-size:18px;line-height:24px}

  .art{position:absolute;left:0;top:0}
</style>
</head>
<body>
<div class="flyer">

  <div class="rule-top"></div>
  <div class="title-band"></div>
  <div class="rule-bottom"></div>

  <svg class="art" width="945" height="1200" viewBox="0 0 945 1200">
    <defs>
      <linearGradient id="bench" x1="0" y1="0" x2="1" y2="1">
        <stop offset="0" stop-color="#cdb48a"/>
        <stop offset=".45" stop-color="#8c7656"/>
        <stop offset=".7" stop-color="#c9b72e"/>
        <stop offset="1" stop-color="#4a3f33"/>
      </linearGradient>
      <radialGradient id="studio" cx=".5" cy=".5" r=".6">
        <stop offset="0" stop-color="#e6e9ed"/>
        <stop offset="1" stop-color="#ffffff"/>
      </radialGradient>
      <linearGradient id="kit" x1="0" y1="0" x2="1" y2="1">
        <stop offset="0" stop-color="#f4f4f2"/>
        <stop offset=".5" stop-color="#b9b8ae"/>
        <stop offset="1" stop-color="#f1f1ef"/>
      </linearGradient>
    </defs>

    <g role="img" aria-label="Photo: technician calibrating a backflow test gauge at a workbench">
      <circle cx="763" cy="257" r="283" fill="url(#bench)"/>
    </g>
    <path d="M473 257 A290 290 0 0 1 1053 257" fill="none" stroke="var(--blue)" stroke-width="14"/>
    <path d="M1053 257 A290 290 0 0 1 473 257" fill="none" stroke="var(--red)" stroke-width="14"/>

    <g role="img" aria-label="Photo: differential pressure test gauge with coloured hoses">
      <circle cx="805" cy="550" r="106" fill="url(#studio)"/>
    </g>
    <path d="M695 550 A110 110 0 0 1 915 550" fill="none" stroke="var(--blue)" stroke-width="7"/>
    <path d="M915 550 A110 110 0 0 1 695 550" fill="none" stroke="var(--red)" stroke-width="7"/>

    <g role="img" aria-label="Photo: handheld digital backflow test gauge">
      <circle cx="583" cy="705" r="96" fill="url(#studio)"/>
    </g>
    <path d="M483 705 A100 100 0 0 1 683 705" fill="none" stroke="var(--blue)" stroke-width="7"/>
    <path d="M683 705 A100 100 0 0 1 483 705" fill="none" stroke="var(--red)" stroke-width="7"/>

    <g role="img" aria-label="Photo: analog test gauge in an open carry case with hoses">
      <circle cx="788" cy="752" r="118" fill="url(#studio)"/>
    </g>
    <path d="M666 752 A122 122 0 0 1 910 752" fill="none" stroke="var(--blue)" stroke-width="7"/>
    <path d="M910 752 A122 122 0 0 1 666 752" fill="none" stroke="var(--red)" stroke-width="7"/>

    <g role="img" aria-label="Photo: backflow test kit toolbox with gauge and coloured hoses">
      <rect x="597" y="872" width="300" height="222" rx="30" fill="url(#kit)"/>
    </g>
  </svg>

  <div class="brand">
    <span class="brand-mark"></span>
    <span class="brand-name"><span class="line1">Northfield Valve</span><span class="line2">Supply Company</span></span>
  </div>

  <p class="tagline">The Nation’s Leading Source for:</p>

  <h1 class="title">Backflow<br>Prevention Test<br>Gauge Calibration<br>Service</h1>

  <p class="intro">We specializes in backflow prevention, a backflow preventer is a valve on the public drinking water system that prevents contamination. Backflow preventers need to be tested annually using a backflow test gauge. A backflow test gauge is considered an instrument and is required to be tested and calibrated annually to ensure they are working accurately.</p>

  <h2 class="why-head">WHY CHOOSE US</h2>

  <ul class="benefits">
    <li class="benefit" style="--w:400px">
      <svg viewBox="0 0 26 26"><rect x="1" y="7" width="13" height="11" fill="var(--red)"/><path d="M15 10h5l4 4v4h-9z" fill="var(--blue)"/><circle cx="6" cy="20" r="2.5" fill="var(--blue)"/><circle cx="19" cy="20" r="2.5" fill="var(--blue)"/></svg>
      HASSLE FREE SHIPPING</li>
    <li class="benefit" style="--w:430px">
      <svg viewBox="0 0 26 26"><circle cx="13" cy="13" r="11" fill="none" stroke="var(--blue)" stroke-width="2.2" stroke-dasharray="52 8"/><text x="13" y="17" text-anchor="middle" font-family="Noto Sans,sans-serif" font-weight="800" font-size="10" fill="var(--red)">24</text></svg>
      1-DAY TURNAROUND TIME</li>
    <li class="benefit" style="--w:530px">
      <svg viewBox="0 0 26 26"><circle cx="13" cy="13" r="11" fill="none" stroke="var(--blue)" stroke-width="3" stroke-dasharray="4 2.5"/><circle cx="13" cy="13" r="7" fill="#fff" stroke="var(--red)" stroke-width="1.6"/><path d="M13 13l3-3" stroke="var(--red)" stroke-width="1.6"/></svg>
      SERVICE ALL GAUGE MODELS</li>
    <li class="benefit" style="--w:533px">
      <svg viewBox="0 0 26 26"><path d="M6 8l9-5 9 5v11l-9 5-9-5z" fill="var(--blue)"/><path d="M15 13v11M6 8l9 5 9-5" stroke="#fff" stroke-width="1.3" fill="none"/><path d="M2 16a5 5 0 0 0 5 7" stroke="var(--red)" stroke-width="1.8" fill="none"/></svg>
      PRICE INCLUDES INCOMING &amp; RETURN FREIGHT</li>
    <li class="benefit" style="--w:0px">
      <svg viewBox="0 0 26 26"><circle cx="13" cy="10" r="8" fill="none" stroke="var(--blue)" stroke-width="2.2"/><path d="M9 10l3 3 5-6" stroke="var(--red)" stroke-width="2.2" fill="none"/><path d="M8 17l-2 7 4-2 3 3M18 17l2 7-4-2-3 3" fill="var(--blue)"/></svg>
      HONOR ALL MANUFACTURER WARRANTIES</li>
  </ul>

  <p class="details">We offer that service, along with repair services if the instrument is damaged, and we refer to it as a <strong>“Hassle Free”</strong> service. We schedule the service for them once they provide their information and then email them a shipping label that they can print out, tape on their box and send the package from their business or home. We have a quick-turnaround time for this service because we understand how important this piece of equipment is for our customers to continue their job.</p>

  <div class="makers">
    <span class="maker">Halden</span>
    <span class="maker">Korvex</span>
    <span class="maker">Plainfield</span>
    <span class="maker">Trescott</span>
  </div>

  <div class="footer"></div>
  <p class="footer-text">TWO WAYS TO SCHEDULE THIS SERVICE WITH US.<br><span class="big">CALL US OR FILL OUT A FORM ON OUR WEBSITE</span></p>
  <div class="contact">
    <span class="phone">(800) 642-3871</span>
    <span class="web">www.pipeguardshop.com</span>
  </div>

</div>
</body>
</html>
```